NEW Escape Room. Fun, Dark and Mysterious.

Escape Room Website. Bookings and scheduling of appointments will be organised with Bookvane through the site. Most appointments will be created online through the booking system with some payments coming through in person by drop-ins. Groups will be from 2 - 8 people with a sliding scale of prices. We will start with one game playable and one saying coming soon. We will also eventually have 4 games up and running at once so will need it to be able to expand. We don't have any images of the rooms because it all relies heavily on mystery. Appointments are each 1 hour long with 30 minutes in between.

Target Market(s)

15-35 year olds

Coding

Coded - Design and coding required

Number of Pages Required

5+ page

Font styles to use
Decorative

Colors

Designer to choose colors to be used in the design.

Requirements
Must have
• Graphics showing what an escape room is.
• Page for About - What is an escape room
• Page for Games - Showing each of the different games which can be played with links to booking page. We have one game to start - the surgeons shadows. A victorian doctors office and serial killers. Then a game coming soon which is aztec/mayan/jungle/harold Crane feel.
• FAQ Page
Nice to have
• Graphics for multiple players ie 2 players, 3 players, 4 players etc
• Dark and Mysterious feel.
• Inspiration from Puzzle Vault, Cipher Lodge, Quest Lockbox
Should not have
• Cartoony/childish. Pink.
• Not bloody or dripping letters etc - not cliche.
• Not horror themed.

```html
<!DOCTYPE html>
<html lang="en">
<head>
<meta charset="utf-8">
<title>Exit Hollow — Escape Room</title>
<link rel="stylesheet" href="https://fonts.googleapis.com/css2?family=Roboto+Slab:wght@700&family=Poppins:wght@500;600;700&family=Open+Sans:wght@400&display=swap">
<style>
:root{
  --black:#000;
  --ink:#111111;
  --panel:#161616;
  --orange:#e88a2c;
  --orange-deep:#c45f1f;
  --rust:#8a2a18;
  --gold:#d39a3c;
  --white:#ffffff;
  --muted:#c9c9c9;
  --soft:#a8a8a8;
}
*{box-sizing:border-box;margin:0;padding:0}
html,body{width:1200px;height:2907px;overflow:hidden;background:var(--black)}
body{position:relative;font-family:"Open Sans",sans-serif;color:var(--white)}
.abs{position:absolute}
.slab{font-family:"Roboto Slab",serif;font-weight:700}
.pop{font-family:"Poppins",sans-serif}

/* hero */
.hero-bg{left:0;top:0;width:1200px;height:841px;
  background:radial-gradient(ellipse at 50% 45%,#3a3a3a 0%,#222 35%,#0d0d0d 75%,#050505 100%)}
.nav a{position:absolute;top:48px;font-family:"Poppins",sans-serif;font-weight:600;font-size:16px;color:var(--white);text-decoration:none;letter-spacing:.3px;white-space:nowrap}
.nav a.active{color:var(--gold)}
.nav .sep{position:absolute;top:50px;width:1px;height:20px;background:#bbb}
.brand{left:500px;top:100px;width:200px;text-align:center;font-family:"Poppins",sans-serif;font-weight:700;font-size:20px;color:var(--gold);letter-spacing:1px;white-space:nowrap}
.brand-mark{left:580px;top:40px;width:40px;height:40px;border:2px solid var(--gold);border-radius:50%}
.hero-kicker{left:0;width:1200px;top:290px;text-align:center;font-size:43px;line-height:1.2;color:var(--orange);letter-spacing:1px;white-space:nowrap}
.hero-title{left:0;width:1200px;top:350px;text-align:center;font-size:84px;line-height:1;color:var(--white);letter-spacing:2px;white-space:nowrap}
.btn-solid{left:503px;top:457px;width:197px;height:57px;background:linear-gradient(180deg,#f09a3a,#c9621f);
  font-family:"Poppins",sans-serif;font-weight:600;font-size:18px;letter-spacing:1.5px;display:flex;align-items:center;justify-content:center}

/* escape room intro */
.intro-bg{left:0;top:841px;width:1200px;height:560px;background:var(--ink)}
.intro-art{left:120px;top:730px;width:450px;height:540px}
.intro-title{left:604px;top:876px;font-size:34px;line-height:1.2;letter-spacing:.5px;white-space:nowrap}
.intro-copy{left:606px;top:935px;width:500px;font-size:15.5px;line-height:25px;color:var(--muted)}
.intro-copy p+p{margin-top:27px}
.btn-line{border:2px solid var(--gold);font-family:"Poppins",sans-serif;font-weight:600;display:flex;align-items:center;justify-content:center;letter-spacing:.5px;white-space:nowrap}
.btn-learn{left:615px;top:1166px;width:170px;height:49px;font-size:14px;color:var(--gold)}

/* who can play */
.who-title{left:0;width:1200px;top:1402px;text-align:center;font-size:30px;line-height:1.2}
.who-item .hex{position:absolute;width:90px;height:102px}
.who-item h3{position:absolute;font-family:"Poppins",sans-serif;font-weight:600;font-size:19px;color:var(--orange);letter-spacing:1px}
.who-item p{position:absolute;width:230px;font-size:13px;line-height:22px;color:var(--soft)}

/* how it works */
.how-bg{left:0;top:1780px;width:1200px;height:515px;
  background:radial-gradient(ellipse at 50% 40%,#262626 0%,#171717 45%,#0a0a0a 100%)}
.how-title{left:0;width:1200px;top:1809px;text-align:center;font-size:29px;line-height:1.2;color:var(--orange)}
.how-copy{left:250px;width:700px;top:1856px;text-align:center;font-size:16px;line-height:25px;color:var(--muted)}
.step{position:absolute;width:260px;text-align:center}
.step h3{font-family:"Poppins",sans-serif;font-weight:600;font-size:20px;color:var(--orange);white-space:nowrap}
.step p{margin-top:6px;font-size:13px;line-height:20px;color:var(--muted)}

/* booking */
.book-bg{left:0;top:2295px;width:1200px;height:460px;background:linear-gradient(100deg,#d2702c 0%,#c05a22 45%,#8c2c18 100%)}
.book-title{left:0;width:1200px;top:2375px;text-align:center;font-size:36px;line-height:1.2}
.book-copy{left:250px;width:700px;top:2432px;text-align:center;font-size:16px;line-height:25px;color:#fff1e4}
.btn-book{left:436px;top:2511px;width:349px;height:56px;border-color:var(--white);font-size:16px;letter-spacing:1.5px;color:var(--white)}

/* footer */
.foot-nav a{position:absolute;top:2763px;font-family:"Poppins",sans-serif;font-weight:600;font-size:16px;color:#bdbdbd;text-decoration:none;white-space:nowrap}
.copyright{left:0;width:1200px;top:2800px;text-align:center;font-family:"Poppins",sans-serif;font-size:12px;color:#aaa}
.social{position:absolute;top:2835px;width:33px;height:33px;border:1.5px solid #ddd;border-radius:50%}
.social.first{border-color:var(--orange)}
</style>
</head>
<body>

<!-- hero -->
<div class="abs hero-bg" role="img" aria-label="Dark maze-like corridor of stone blocks seen from below"></div>
<svg class="abs" style="left:0;top:0" width="1200" height="841" viewBox="0 0 1200 841">
  <polygon points="0,627 602,790 1200,627 1200,841 0,841" fill="#000"/>
  <polyline points="0,627 602,790 1200,627" fill="none" stroke="#e88a2c" stroke-width="4"/>
  <polyline points="88,352 72,367 88,382" fill="none" stroke="#fff" stroke-width="4"/>
  <polyline points="1110,352 1126,367 1110,382" fill="none" stroke="#fff" stroke-width="4"/>
</svg>
<nav class="nav">
  <a href="#" class="active" style="left:218px">ABOUT</a>
  <span class="sep" style="left:310px"></span>
  <a href="#" style="left:347px">GAMES</a>
  <a href="#" style="left:773px">CONTACT US</a>
  <span class="sep" style="left:913px"></span>
  <a href="#" style="left:952px">FAQ</a>
</nav>
<div class="abs brand-mark"></div>
<div class="abs brand">EXIT HOLLOW</div>
<div class="abs slab hero-kicker">WELCOME TO</div>
<h1 class="abs slab hero-title">EXIT HOLLOW</h1>
<div class="abs btn-solid">BOOK NOW</div>

<!-- intro -->
<div class="abs intro-bg"></div>
<svg class="abs intro-art" viewBox="0 0 450 540" role="img" aria-label="Creature clutching a hexagon frame around an open doorway glowing with light">
  <defs>
    <radialGradient id="doorGlow" cx="50%" cy="45%" r="55%">
      <stop offset="0" stop-color="#d48a3a"/>
      <stop offset=".4" stop-color="#4a2e18"/>
      <stop offset="1" stop-color="#0c0f16"/>
    </radialGradient>
  </defs>
  <polygon points="224,193 402,296 402,500 224,533 47,500 47,296" fill="url(#doorGlow)" stroke="#e88a2c" stroke-width="2"/>
  <ellipse cx="200" cy="110" rx="95" ry="90" fill="#2a2a2a"/>
</svg>
<h2 class="abs slab intro-title">WHAT AN ESCAPE ROOM</h2>
<div class="abs intro-copy">
  <p>Fusce tellus Sed metus augue convallis et vehicula ut pulvinar eu ante Integer orci tellus tristique vitae consequat nec porta vel lectus Nulla sit amet daliquam enim Proin dui lectus</p>
  <p>Aursus eu mattis laoreet viverra sit amet quam Curabitur vel dolor ultrices ipsum dictum tristique Praesent vitae lacus Ut velit enim vestibulum non fermentum nec hendrerit quis leo Pellentesque rutrum malesuada neque Nunc tempus felis vitae urna</p>
</div>
<div class="abs btn-line btn-learn">LEARN MORE</div>

<!-- who can play band -->
<svg class="abs" style="left:0;top:1300px" width="1200" height="480" viewBox="0 1300 1200 480">
  <defs>
    <linearGradient id="brownBand" x1="0" y1="0" x2="0" y2="1">
      <stop offset="0" stop-color="#3a2516"/>
      <stop offset="1" stop-color="#1a1614"/>
    </linearGradient>
  </defs>
  <polygon points="0,1389 600,1310 1200,1389 1200,1654 602,1756 0,1654" fill="url(#brownBand)"/>
  <polygon points="0,1654 602,1756 1200,1654 1200,1780 0,1780" fill="#0f0f0f"/>
  <polyline points="0,1654 602,1756 1200,1654" fill="none" stroke="#000" stroke-width="6"/>
  <polyline points="0,1662 606,1753 1200,1664" fill="none" stroke="#e88a2c" stroke-width="2"/>
</svg>
<div class="abs how-bg" role="img" aria-label="Dim stone brick corridor"></div>
<h2 class="abs slab who-title">WHO CAN PLAY</h2>

<div class="who-item">
  <svg class="hex" style="left:139px;top:1490px" viewBox="0 0 90 102"><polygon points="45,2 88,26 88,76 45,100 2,76 2,26" fill="none" stroke="#e88a2c" stroke-width="1.5"/><g fill="none" stroke="#e88a2c" stroke-width="2"><circle cx="36" cy="40" r="7"/><circle cx="56" cy="40" r="7"/><path d="M24 66c0-10 6-15 12-15s12 5 12 15M44 66c0-10 6-15 12-15s12 5 12 15"/></g></svg>
  <h3 style="left:245px;top:1506px">FAMILY</h3>
  <p style="left:245px;top:1537px">Arerit quis leo Pellentesque rutrum malesuada neque Nunc tempus</p>
</div>
<div class="who-item">
  <svg class="hex" style="left:490px;top:1490px" viewBox="0 0 90 102"><polygon points="45,2 88,26 88,76 45,100 2,76 2,26" fill="none" stroke="#e88a2c" stroke-width="1.5"/><g fill="none" stroke="#e88a2c" stroke-width="2"><circle cx="32" cy="38" r="6"/><circle cx="58" cy="38" r="6"/><circle cx="45" cy="52" r="6"/><path d="M22 60c0-8 4-12 10-12s10 4 10 12M48 60c0-8 4-12 10-12s10 4 10 12M34 74c0-8 5-12 11-12s11 4 11 12"/></g></svg>
  <h3 style="left:596px;top:1506px">CORPORATE</h3>
  <p style="left:596px;top:1537px">Arerit quis leo Pellentesque rutrum malesuada neque Nunc tempus</p>
</div>
<div class="who-item">
  <svg class="hex" style="left:823px;top:1490px" viewBox="0 0 90 102"><polygon points="45,2 88,26 88,76 45,100 2,76 2,26" fill="none" stroke="#e88a2c" stroke-width="1.5"/><g fill="none" stroke="#e88a2c" stroke-width="2"><circle cx="30" cy="40" r="6"/><circle cx="45" cy="37" r="6"/><circle cx="60" cy="40" r="6"/><path d="M22 70V56c0-5 4-8 8-8s8 3 8 8v14M37 70V53c0-5 4-8 8-8s8 3 8 8v17M52 70V56c0-5 4-8 8-8s8 3 8 8v14"/></g></svg>
  <h3 style="left:929px;top:1506px">FRIENDS</h3>
  <p style="left:929px;top:1537px">Arerit quis leo Pellentesque rutrum malesuada neque Nunc tempus</p>
</div>

<!-- how it works -->
<h2 class="abs slab how-title">HOW IT WORKS</h2>
<p class="abs how-copy">Fusce tellus Sed metus augue convallis et vehicula ut pulvinar eu ante Integer orci tellus tristique vitae consequat nec porta vel lectus Nulla sit amet daliquam enim</p>
<svg class="abs" style="left:0;top:1940px" width="1200" height="170" viewBox="0 1940 1200 170">
  <defs>
    <linearGradient id="ring" x1="0" y1="0" x2="1" y2="1">
      <stop offset="0" stop-color="#e88a2c"/><stop offset="1" stop-color="#8a4a1c"/>
    </linearGradient>
  </defs>
  <line x1="382" y1="2024" x2="518" y2="2024" stroke="#b7652a" stroke-width="2"/>
  <line x1="698" y1="2024" x2="834" y2="2024" stroke="#b7652a" stroke-width="2"/>
  <circle cx="294" cy="2024" r="70" fill="none" stroke="url(#ring)" stroke-width="3"/>
  <circle cx="610" cy="2024" r="70" fill="none" stroke="url(#ring)" stroke-width="3"/>
  <circle cx="926" cy="2024" r="70" fill="none" stroke="url(#ring)" stroke-width="3"/>
  <g fill="none" stroke="#e88a2c" stroke-width="2.5">
    <circle cx="294" cy="2006" r="8"/><circle cx="274" cy="2012" r="7"/><circle cx="314" cy="2012" r="7"/>
    <path d="M278 2044c0-12 7-18 16-18s16 6 16 18M260 2040c0-9 5-14 12-14M328 2040c0-9-5-14-12-14"/>
    <circle cx="610" cy="1998" r="7"/><path d="M610 2005v16M610 2013h6M610 2019h6"/>
    <circle cx="594" cy="2036" r="7"/><path d="M589 2041l-14 14M578 2052l4 4"/>
    <circle cx="628" cy="2036" r="7"/><path d="M633 2041l14 14M644 2052l-4 4"/>
  </g>
  <circle cx="926" cy="2024" r="48" fill="#2a1a10" role="img" aria-label="Creature silhouette icon"/>
</svg>
<div class="step" style="left:164px;top:2110px"><h3>2 TO 6 PLAYERS</h3><p>Apulvinar eu ante Integer orci tellus tristique vitae consequat nec</p></div>
<div class="step" style="left:480px;top:2110px"><h3>45 MINUTES OF GAME</h3><p>Apulvinar eu ante Integer orci tellus tristique vitae consequat nec</p></div>
<div class="step" style="left:796px;top:2110px"><h3>TONS OF ADVENTURE</h3><p>Apulvinar eu ante Integer orci tellus tristique vitae consequat nec</p></div>

<!-- booking -->
<div class="abs book-bg"></div>
<h2 class="abs slab book-title">BOOK APPOINTMENT</h2>
<p class="abs book-copy">Fusce tellus Sed metus augue convallis et vehicula ut pulvinar eu ante Integer orci tellus tristique vitae consequat nec porta vel lectus Nulla sit amet daliquam enim</p>
<div class="abs btn-line btn-book">SCHEDULING OF APPOINTMENTS</div>

<!-- footer -->
<svg class="abs" style="left:0;top:2640px" width="1200" height="267" viewBox="0 2640 1200 267">
  <polygon points="0,2743 560,2660 640,2660 1200,2743 1200,2907 0,2907" fill="#000"/>
  <polyline points="0,2736 560,2668" fill="none" stroke="#e88a2c" stroke-width="2"/>
  <polyline points="640,2668 1200,2736" fill="none" stroke="#e88a2c" stroke-width="2"/>
  <circle cx="600" cy="2676" r="30" fill="#000" stroke="#d39a3c" stroke-width="2"/>
</svg>
<div class="abs pop" style="left:520px;top:2712px;width:160px;text-align:center;font-weight:700;font-size:14px;color:var(--gold);letter-spacing:.5px;white-space:nowrap">EXIT HOLLOW</div>
<nav class="foot-nav">
  <a href="#" style="left:322px">HOME</a>
  <a href="#" style="left:436px">ABOUT</a>
  <a href="#" style="left:558px">GAMES</a>
  <a href="#" style="left:681px">CONTACT US</a>
  <a href="#" style="left:860px">FAQ</a>
</nav>
<div class="abs copyright">© 2020 Company Name | All Rights Reserved | Disclaimer</div>
<span class="social first" style="left:524px"></span>
<span class="social" style="left:562px"></span>
<span class="social" style="left:602px"></span>
<span class="social" style="left:641px"></span>

</body>
</html>
```